LUMETTE INC. is a new Fashion Stylist, Design Merchandiser, and consultant in the fashion industry

We need a logo design for a new Calgary, Alberta based company that is in the business of making over your image, wardrobe and style for both business and personal purposes.

Target Market(s)

Professional female and male business people looking for a new style or complete fashion makeover including clothes closet merchandising and makeover.

Contact Information for Business Card

see the uploaded file

Number of Pages Required

1 page

Font styles to use
Script

Colors
fac994
fbe7d2
fee3d4

Requirements
Must have
• Fashion Industry theme that is very elegant and colorful using gold/bronze/silver color themes.
Nice to have
• Incorporate the company name with the creative font to come up with the appropriate "logo"

```html
<!DOCTYPE html>
<html lang="en">
<head>
<meta charset="utf-8">
<title>LUMETTE INC. Business Cards</title>
<link rel="stylesheet" href="https://fonts.googleapis.com/css2?family=Open+Sans:wght@300;400;600&display=swap">
<style>
  :root {
    --backdrop: #3a3a3a;
    --card-dark: #1c1c1c;
    --card-light: #f4f4f4;
    --gold: #a8946a;
    --gold-soft: #c9b68c;
    --ink: #2a2a2a;
    --ink-light: #e9e9e9;
    --muted: #6b6b6b;
  }
  * { box-sizing: border-box; margin: 0; padding: 0; }
  html, body { width: 1200px; height: 716px; overflow: hidden; }
  body {
    background: var(--backdrop);
    font-family: "Open Sans", sans-serif;
    position: relative;
  }
  .card {
    position: absolute;
    top: 208px;
    width: 520px;
    height: 300px;
    border-radius: 3px;
    box-shadow: 0 10px 28px rgba(0,0,0,.45);
  }
  .card--front { left: 50px; background: var(--card-dark); }
  .card--back { left: 630px; background: var(--card-light); }

  .brand {
    position: absolute;
    display: flex;
    align-items: center;
    gap: 14px;
  }
  .brand__dot {
    width: 14px; height: 14px;
    border-radius: 50%;
    background: var(--gold);
    flex: none;
  }
  .brand__name {
    font-weight: 300;
    font-size: 40px;
    letter-spacing: 2px;
    line-height: 1;
  }
  .brand__tagline {
    position: absolute;
    font-size: 9px;
    font-weight: 400;
    letter-spacing: .5px;
  }
  .card--front .brand { left: 90px; top: 96px; }
  .card--front .brand__name { color: var(--ink-light); }
  .card--front .brand__tagline { left: 118px; top: 146px; color: var(--gold-soft); }
  .website-front {
    position: absolute;
    left: 0; right: 0; top: 220px;
    text-align: center;
    color: var(--gold);
    font-size: 14px;
    letter-spacing: 4px;
  }

  .card--back .brand { left: 34px; top: 48px; }
  .card--back .brand__name { color: var(--ink); }
  .card--back .brand__tagline { left: 62px; top: 98px; color: var(--muted); }

  .holder {
    position: absolute;
    right: 36px; top: 150px;
    font-size: 19px;
    font-weight: 600;
    color: var(--ink);
  }
  .contact {
    position: absolute;
    display: flex;
    align-items: center;
    gap: 10px;
    font-size: 14px;
    color: var(--ink);
  }
  .contact svg { width: 16px; height: 16px; fill: none; stroke: var(--gold); stroke-width: 1.6; flex: none; }
  .contact--email { left: 34px; top: 196px; }
  .contact--web { left: 200px; top: 236px; }
  .contact--phone { left: 350px; top: 264px; }
</style>
</head>
<body>
  <section class="card card--front">
    <div class="brand">
      <span class="brand__dot"></span>
      <span class="brand__name">LUMETTE INC.</span>
    </div>
    <p class="brand__tagline">Fashion Stylist | Design Merchandiser | Consultant</p>
    <p class="website-front">www.lumette-inc.ca</p>
  </section>

  <section class="card card--back">
    <div class="brand">
      <span class="brand__dot"></span>
      <span class="brand__name">LUMETTE INC.</span>
    </div>
    <p class="brand__tagline">Fashion Stylist | Design Merchandiser | Consultant</p>

    <p class="holder">Marisol Hendrikse</p>

    <p class="contact contact--email">
      <svg viewBox="0 0 16 16" aria-hidden="true"><rect x="1.5" y="3.5" width="13" height="9"/><path d="M1.5 3.5 8 9l6.5-5.5"/></svg>
      marisol@lumette-inc.com
    </p>
    <p class="contact contact--web">
      <svg viewBox="0 0 16 16" aria-hidden="true"><circle cx="8" cy="8" r="6.5"/><ellipse cx="8" cy="8" rx="2.8" ry="6.5"/><path d="M1.5 8h13"/></svg>
      www.lumette-inc.ca
    </p>
    <p class="contact contact--phone">
      <svg viewBox="0 0 16 16" aria-hidden="true"><path d="M4 2.5h2l1 3-1.5 1a8 8 0 0 0 4 4l1-1.5 3 1v2a1.5 1.5 0 0 1-1.5 1.5A11 11 0 0 1 2.5 4 1.5 1.5 0 0 1 4 2.5z"/></svg>
      (403)555-0142
    </p>
  </section>
</body>
</html>
```